Geschäftspapiere für Fliesenleger - Meisterbetrieb
Zielgruppe
Wir sind ein mittelständischer Fliesenleger - Meisterbetrieb und möchten unsere Geschäftspapiere erneuern. Unsere Kunden sind Privatkunden, Gewerbetreibende sowie Öffentliche Auftraggeber.
Aufgabenstellung
Unser Logo stellen wir Ihnen zur verfügung und soll unverändert bleiben.
Wir benötigen folgende Geschäftspapiere:
- Briefpapier DIN A4
- Notizblock Karriert DIN A4
- Visitenkarten 5,5 x 8,5 cm
- Kuvert DIN lang mit Fenster
- Kuvert DIN C4 mit Fenster
Bei der Farbe Rot handelt es sich um Verkehrsrot RAL 3020
Als Schriftart haben wir uns Helvetica Neue vorgestellt.
Wir bitten jedoch auch um Vorschläge anderer Moderner und gut lesbarer Schriftarten die für Print und Web bestens geeignet sind.
Wir wünschen uns ein Modernes und Schnörkelloses Design. Bei den Dateien habe ich Ihnen ein Stockphoto angehängt um Ihnen zu zeigen wie wir uns ein Cover oder eine Broschüre vorstellen können. Nur um Ihnen unsere Ideen / Vorstellungen näher zu bringen.

```html
<!DOCTYPE html>
<html lang="de">
<head>
<meta charset="utf-8">
<title>Fliesen-Kerner – Geschäftspapiere</title>
<link href="https://fonts.googleapis.com/css2?family=Arimo:wght@400;700&display=swap" rel="stylesheet">
<style>
:root{
  --red:#c8201e;
  --ink:#111;
  --paper:#fff;
  --bg:#fff;
  --window:#ececec;
  --grid:#d6d6d6;
  --shadow:0 1px 6px rgba(0,0,0,.14);
}
*{box-sizing:border-box;margin:0;padding:0}
html,body{width:750px;height:1200px;overflow:hidden;background:var(--bg)}
body{position:relative;font-family:"Arimo",Helvetica,Arial,sans-serif;color:var(--ink)}
.sheet{position:absolute;background:var(--paper);box-shadow:var(--shadow);overflow:hidden}
.wordmark{position:absolute;display:flex;align-items:center;gap:.3em;font-weight:700;color:var(--ink);white-space:nowrap;line-height:1}
.wordmark::before{content:"";width:.45em;height:.45em;background:var(--red)}
.red{color:var(--red)}
.tile-art{position:absolute;left:0;background:linear-gradient(135deg,#fff 0%,#e9a3a2 45%,var(--red) 100%)}
/* main letter */
.letter{left:78px;top:41px;width:539px;height:763px}
.letter .wordmark{right:38px;top:110px;font-size:22px}
.sender{position:absolute;left:64px;top:135px;font-size:6.4px}
.recipient{position:absolute;left:64px;top:156px;font-size:9.6px;line-height:12px}
.date{position:absolute;left:64px;top:243px;font-size:9.6px}
.fold{position:absolute;left:0;top:270px;width:8px;border-top:.6px solid #444}
.subject{position:absolute;left:64px;top:276px;font-size:9.6px;font-weight:700}
.body{position:absolute;left:64px;top:308px;width:385px;font-size:9.6px;line-height:12px}
.body p{margin-bottom:12px}
.letter .tile-art{top:652px;width:54px;height:84px}
.footer{position:absolute;left:64px;top:700px;display:flex;font-size:6.3px;line-height:8.6px}
.footer div{flex:none}
.footer b{font-weight:700}
.f1{width:88px}.f2{width:104px}.f3{width:148px}
.contact span{display:inline-block;width:10px;font-weight:700}
/* business card */
.card{left:531px;top:220px;width:181px;height:117px}
.card .wordmark{left:53px;top:30px;font-size:14px}
.card .name{position:absolute;left:53px;top:54px;font-size:7px;font-weight:700}
.card .role{position:absolute;left:53px;top:63px;font-size:5px}
.card .info{position:absolute;left:53px;top:80px;display:flex;gap:10px;font-size:4.8px;line-height:7px}
.card .contact span{width:8px}
.card .tile-art{top:42px;width:45px;height:70px}
/* miniatures */
.mini{font-size:2.2px;line-height:3px}
.mini-letter{left:60px;top:906px;width:174px;height:246px}
.mini-letter .wordmark{right:12px;top:25px;font-size:7px}
.mini-letter .sender{left:21px;top:45px;font-size:2.1px}
.mini-letter .fold{top:87px;width:3px}
.mini-letter .tile-art{top:212px;width:18px;height:28px}
.mini-letter .mfoot{position:absolute;left:21px;top:225px;display:flex;gap:8px}
.mini-card{left:202px;top:962px;width:65px;height:42px}
.mini-card .wordmark{left:19px;top:11px;font-size:5px}
.mini-card .mtext{position:absolute;left:19px;top:20px;font-size:1.9px;line-height:2.6px}
.mini-card .tile-art{top:18px;width:16px;height:22px}
.mini-pad{left:285px;top:906px;width:174px;height:246px}
.mini-pad .wordmark{right:11px;top:17px;font-size:7px}
.mini-pad .lines{position:absolute;left:11px;top:14px;width:54px;height:10px;border-top:1px solid var(--grid);border-bottom:1px solid var(--grid)}
.mini-pad .grid{position:absolute;left:11px;top:30px;width:152px;height:198px;border:1px solid var(--grid);
  background-image:linear-gradient(to bottom,var(--grid) 1px,transparent 1px),linear-gradient(to right,var(--grid) 1px,transparent 1px);
  background-size:5px 5px}
.mini-pad .tile-art{top:214px;width:18px;height:28px}
.mini-pad .mfoot{position:absolute;left:64px;top:234px;display:flex;gap:8px}
.env-c4{left:478px;top:885px;width:190px;height:268px}
.env-c4 .wordmark{left:42px;top:20px;font-size:7.5px}
.env-c4 .tile-art{top:4px;width:18px;height:28px}
.env-window{position:absolute;background:var(--window);border-radius:2px;padding:5px 8px}
.env-c4 .env-window{left:14px;top:45px;width:77px;height:47px}
.env-window .ws{font-size:1.8px;margin-bottom:4px}
.env-window .wr{font-size:2.6px;line-height:3.4px}
.env-c4 .url{position:absolute;right:13px;bottom:12px;font-size:2.4px;font-weight:700}
.env-dl{left:525px;top:1025px;width:187px;height:93px}
.env-dl .wordmark{left:53px;top:20px;font-size:6.5px}
.env-dl .tile-art{top:8px;width:17px;height:26px}
.env-dl .env-window{left:16px;top:43px;width:77px;height:37px}
</style>
</head>
<body>

<section class="sheet letter">
  <div class="wordmark">Fliesen-Kerner</div>
  <p class="sender"><span class="red">KRTD Kerner GmbH</span> · Lindenhofweg 48 · 91287 Wiesental</p>
  <p class="recipient">Herr<br>Max Mustermann<br>Musterstraße 12<br>12345 Musterstadt</p>
  <p class="date">Wiesental, 5. Mai 2025</p>
  <div class="fold"></div>
  <p class="subject">Betreff: Briefbogen</p>
  <div class="body">
    <p>Sehr geehrter Herr Mustermann,</p>
    <p>falls Sie keine Probleme haben, diesen Blindtext schnell und zügig zu lesen, können Sie sich glücklich schätzen. Der verantwortliche Art Director, der Ihnen höchstwahrscheinlich gerade diesen Entwurf präsentiert, versteht sein typografisches Handwerk par excellence.</p>
    <p>Er hat diesen Copyblock weder gestaucht, gezerrt, noch in Versalien oder gar in 6 Punkt Zierstile Outline gesetzt. Er hat ihn ganz einfach lesbar gemacht. Offenbar sogar ziemlich gut, sonst hätten Sie wohl schon einige Zeilen zuvor die Leselust verloren. Beachten Sie nur die Zeilenbreite, die er gewählt hat. Sie ist weder zu lang noch zu kurz gewählt.</p>
    <p>Der dazugehörige Zeilenabstand ist ideal. Ihre Augen haben keinerlei Probleme, vom Ende einer Zeile in die nächste zu gelangen. Um einen solchen Art Director kann man Sie beneiden. Er nutzt den ihm gewährten gestalterischen Freiraum nicht, um sich selbst darzustellen, sondern Sie. Er weiß, daß es Wichtiges über Ihr Unternehmen oder Produkt zu sagen gibt.</p>
    <p>Und dem räumt er großzügig Platz ein. Dieser Mensch hat zweifelsohne nicht am Mäschäßutzets Inschtitut of Gräfick Ahts studiert. Er besitzt keine Bücher von Nevin Brandt oder Aprila Grimm, und wenn doch, ordnet er sie im Regal unter Kunst ein. Statt dessen pflegt er eine liebevoll innige Beziehung zu Büchern von Tschirner und Olt Eichner. Er liest sie.</p>
    <p>Mit recht freundlichen Grüßen</p>
    <p>Lorenz Kerner</p>
  </div>
  <div class="tile-art" role="img" aria-label="Dekoratives Fliesenmotiv in Rot"></div>
  <div class="footer">
    <div class="f1"><b class="red">KRTD Kerner GmbH</b><br><br>Lindenhofweg 48<br>91287 Wiesental</div>
    <div class="f2 contact"><span>T</span>09183 - 47 20 310<br><span>F</span>09183 - 47 20 399<br><span>M</span>post@fliesen-kerner.de<br><span>W</span>www.fliesen-kerner.de</div>
    <div class="f3"><b>Bankverbindung</b><br>Talgrund Volksbank – Auenstadt<br>IBAN: DE00 0000 0000 0000 0000 00<br>BIC: GENODEF1TLG</div>
    <div><b>Geschäftsführer</b><br>Lorenz Kerner<br>HRB 4412 Amtsgericht Auenstadt<br>Ust. ID: DE902745118</div>
  </div>
</section>

<section class="sheet card">
  <div class="wordmark">Fliesen-Kerner</div>
  <p class="name">Lorenz Kerner</p>
  <p class="role">Geschäftsführer</p>
  <div class="tile-art" role="img" aria-label="Dekoratives Fliesenmotiv in Rot"></div>
  <div class="info">
    <div><b class="red">KRTD Kerner GmbH</b><br><br>Lindenhofweg 48<br>91287 Wiesental</div>
    <div class="contact"><span>T</span>09183 - 47 20 310<br><span>F</span>09183 - 47 20 399<br><span>M</span>post@fliesen-kerner.de<br><span>W</span>www.fliesen-kerner.de</div>
  </div>
</section>

<section class="sheet mini mini-letter">
  <div class="wordmark">Fliesen-Kerner</div>
  <p class="sender"><span class="red">KRTD Kerner GmbH</span> · Lindenhofweg 48 · 91287 Wiesental</p>
  <div class="fold"></div>
  <div class="tile-art" role="img" aria-label="Dekoratives Fliesenmotiv in Rot"></div>
  <div class="mfoot">
    <div><b class="red">KRTD Kerner GmbH</b><br>Lindenhofweg 48<br>91287 Wiesental</div>
    <div>T 09183 - 47 20 310<br>F 09183 - 47 20 399<br>M post@fliesen-kerner.de<br>W www.fliesen-kerner.de</div>
    <div><b>Bankverbindung</b><br>Talgrund Volksbank<br>IBAN: DE00 0000 0000 00<br>BIC: GENODEF1TLG</div>
    <div><b>Geschäftsführer</b><br>Lorenz Kerner<br>HRB 4412 Auenstadt<br>DE902745118</div>
  </div>
</section>

<section class="sheet mini mini-card">
  <div class="wordmark">Fliesen-Kerner</div>
  <div class="mtext"><b>Lorenz Kerner</b><br>Geschäftsführer<br><span class="red">KRTD Kerner GmbH</span> · T 09183 - 47 20 310<br>Lindenhofweg 48 · post@fliesen-kerner.de<br>91287 Wiesental · www.fliesen-kerner.de</div>
  <div class="tile-art" role="img" aria-label="Dekoratives Fliesenmotiv in Rot"></div>
</section>

<section class="sheet mini mini-pad">
  <div class="lines"></div>
  <div class="wordmark">Fliesen-Kerner</div>
  <div class="grid"></div>
  <div class="tile-art" role="img" aria-label="Dekoratives Fliesenmotiv in Rot"></div>
  <div class="mfoot">
    <div><b class="red">KRTD Kerner GmbH</b></div>
    <div>Lindenhofweg 48<br>91287 Wiesental</div>
    <div>T 09183 - 47 20 310<br>F 09183 - 47 20 399</div>
    <div>M post@fliesen-kerner.de<br>W www.fliesen-kerner.de</div>
  </div>
</section>

<section class="sheet mini env-c4">
  <div class="tile-art" role="img" aria-label="Dekoratives Fliesenmotiv in Rot"></div>
  <div class="wordmark">Fliesen-Kerner</div>
  <div class="env-window">
    <p class="ws"><span class="red">KRTD Kerner GmbH</span> · Lindenhofweg 48 · 91287 Wiesental</p>
    <p class="wr">Herr<br>Max Mustermann<br>Musterstraße 12<br>12345 Musterstadt</p>
  </div>
  <p class="url">www.fliesen-kerner.de</p>
</section>

<section class="sheet mini env-dl">
  <div class="tile-art" role="img" aria-label="Dekoratives Fliesenmotiv in Rot"></div>
  <div class="wordmark">Fliesen-Kerner</div>
  <div class="env-window">
    <p class="ws"><span class="red">KRTD Kerner GmbH</span> · Lindenhofweg 48 · 91287 Wiesental</p>
    <p class="wr">Herr<br>Max Mustermann<br>Musterstraße 12<br>12345 Musterstadt</p>
  </div>
</section>

</body>
</html>
```